Drug safety monitoring company requires a new corporate website

We are an outsourcing partner to large and small companies within the pharmaceutical industry. Our current website www.quorvanta.co.uk has not been updated in a long time. We want a new web site that is responsive and modern but with a clearly corporate and professional feel. We want a design based on a 12 column grid system (mobile and desktop version). We want to use a new, modern font (not the standard web fonts) - we will purchase as required. Content can be used as is from the current website. Red and white are the corporate colours, so a palate should be developed to match. We do not need as much red as is in the current website. New icons (preferably in svg format) would be great. We can also purchase new images from Framly (or other) as required. We would prefer submissions in Sketch if possible.

Target Market(s)

Pharmaceutical companies

Number of Pages Required

1 page

Font styles to use
Sans Serif

Colors
ec1f27
ffffff

Requirements
Must have
• Design based on 12 column grid system.
Responsive design (i.e. require a mobile and desktop version).
How should the menu look between desktop and mobile?
A coherent colour palete.
Content to come from the existing website: www.quorvanta.co.uk
How should links be styled?
How should headings, sub-headings, paragraphs be styled?
Nice to have
• Custom developed icons (these are along the bottom of the page on the existing website: Medical Information; Pharmacovigilance; Literature Monitoring; Training).
New imagery (the images on the current website are dated).
Submission ideally as Sketch files (but we are okay with photoshop too).
A new, modern, non-standard font.
Not so much red in the design.
If we had buttons on the website, how should they be styled?
If we had a form on the website, how should the fields be styled?

```html
<!DOCTYPE html>
<html lang="en">
<head>
<meta charset="utf-8">
<title>Quorvanta Pharmacovigilance – Desktop and Mobile</title>
<link href="https://fonts.googleapis.com/css2?family=Poppins:wght@300;400;500;600;700&display=swap" rel="stylesheet">
<style>
:root{
  --red:#ec1f27;
  --white:#ffffff;
  --ink:#111418;
  --text:#6b6f76;
  --line:#e6e7ea;
  --navy:#232a35;
  --navy-deep:#1c222b;
  --stage:#cdd3de;
}
*{margin:0;padding:0;box-sizing:border-box}
html,body{width:865px;height:1200px;overflow:hidden}
body{background:var(--stage);font-family:'Poppins',sans-serif;color:var(--ink);position:relative}
.abs{position:absolute}
.screen{position:absolute;background:var(--white);overflow:hidden}
.desktop{left:64px;top:56px;width:441px;height:1057px}
.mobile{left:590px;top:69px;width:181px;height:928px;border-radius:0 0 14px 14px}

/* top bar */
.topbar{left:0;top:0;width:100%;height:17px;border-bottom:1px solid var(--line);font-size:4.3px;color:var(--text)}
.topbar span{position:absolute;top:6px;display:flex;align-items:center;gap:2px}
.topbar b{color:var(--ink);font-weight:600}
.dots{position:absolute;top:6px;right:37px;display:flex;gap:5px}
.dot{width:4px;height:4px;border-radius:50%;background:var(--red)}

.brand{font-weight:600;color:var(--red);letter-spacing:.08em}
.brand-sub{font-size:2.6px;color:var(--red);letter-spacing:.1em;font-weight:500}

.nav{left:0;top:17px;width:100%;height:36px;border-bottom:1.2px solid var(--red)}
.nav ul{position:absolute;right:37px;top:13px;display:flex;gap:10px;list-style:none;font-size:4.4px;color:var(--text)}
.nav li.active{color:var(--red);border-bottom:.8px solid var(--red);padding-bottom:2px}

.photo{position:absolute}
.hero{left:0;top:53px;width:100%;height:176px;background:linear-gradient(90deg,#6a6f73 0%,#8b9095 35%,#c9ccce 65%,#a9b0b6 100%)}
.hero-text{position:absolute;left:37px;top:48px;color:var(--white)}
.kicker{font-weight:300;font-size:12px;line-height:1.1}
.title{font-weight:700;font-size:16px;line-height:1.15}
.lead{font-size:4.4px;line-height:1.7;margin-top:6px}
.btn{display:inline-flex;align-items:center;gap:2px;background:var(--red);color:var(--white);border-radius:8px;font-size:4.3px;padding:3px 7px;margin-top:12px;font-weight:500}

.divider{position:absolute;left:50%;transform:translateX(-50%);display:flex;align-items:center;gap:8px}
.divider i{display:block;width:65px;height:.6px;background:var(--line)}
.divider .brand{font-size:5px;border:.6px solid var(--red);border-radius:4px;padding:0 4px}

.heading{position:absolute;left:0;width:100%;text-align:center;font-weight:600;font-size:11.5px;line-height:1.25}
.heading em{font-style:normal;color:var(--red)}
.para{position:absolute;text-align:center;font-size:4.2px;line-height:1.8;color:var(--text)}

.card{position:absolute;top:341px;width:68px;height:114px;background:var(--white);box-shadow:0 1px 6px rgba(0,0,0,.08);border-bottom:1px solid var(--red);text-align:center;padding:12px 6px 0}
.card.is-active{background:var(--red);color:var(--white)}
.card .icon{width:26px;height:26px;margin:0 auto;border-radius:50%;background:var(--red);display:flex;align-items:center;justify-content:center;box-shadow:0 2px 5px rgba(236,31,39,.35)}
.card.is-active .icon{background:var(--white);box-shadow:0 2px 5px rgba(0,0,0,.2)}
.card h3{font-size:5.2px;font-weight:500;margin-top:12px}
.card p{font-size:4.3px;line-height:1.75;color:var(--text);margin-top:8px}
.card.is-active p{color:var(--white)}

.gpp{left:0;top:496px;width:100%;height:176px;background:linear-gradient(90deg,#cfd8de 0%,#eef3f6 45%,#d9eef4 75%,#a5e0ee 100%)}
.gpp-text{position:absolute;right:37px;top:48px;text-align:right}
.gpp-text .kicker{color:var(--ink)}
.gpp-text .title{color:var(--ink);font-size:16px}
.gpp-text .lead{color:var(--ink)}

.person{position:absolute;text-align:center;width:80px}
.avatar{width:76px;height:76px;margin:0 auto;border-radius:50%;border:1px solid var(--red);padding:3px}
.avatar div{width:100%;height:100%;border-radius:50%;background:radial-gradient(circle at 50% 45%,#d8c2b0 0%,#c9d3da 60%,#e6ecf0 100%)}
.person h4{font-size:5px;font-weight:500;margin-top:11px}
.person p{font-size:4.2px;color:var(--text);line-height:1.8;margin-top:2px}

.footer{left:0;top:912px;width:100%;height:121px;background:var(--navy);color:#cfd3da;font-size:4.3px}
.footer h5{font-size:4.8px;font-weight:500;color:var(--white)}
.footer .brand{color:var(--white)}
.social{display:flex;gap:9px}
.social i{display:block;width:4.5px;height:4.5px;border-radius:50%;background:var(--white)}
.footer a{color:var(--white);text-decoration:underline}
.footer ul{list-style:none;text-align:right;line-height:2.15}
.copy{left:0;width:100%;background:var(--navy-deep);color:var(--white);text-align:center}

/* mobile */
.m-head{left:0;top:0;width:100%;height:55px;border-bottom:1.2px solid var(--red)}
.m-hero{left:0;top:55px;width:100%;height:109px;background:linear-gradient(90deg,#777b7f 0%,#999ea2 45%,#c2c6c9 75%,#a4abb1 100%)}
.mobile .kicker{font-size:9px}
.mobile .title{font-size:12px}
.mobile .lead{font-size:3.1px;margin-top:5px}
.mobile .btn{font-size:3.1px;padding:2px 5px;margin-top:8px}
.mobile .heading{font-size:8.5px}
.mobile .para{font-size:3px}
.mobile .card{width:69px;height:115px;top:251px;padding-top:12px}
.mobile .card .icon{width:24px;height:24px}
.mobile .card h3{font-size:4.8px;margin-top:14px}
.mobile .card p{font-size:4.2px;margin-top:8px}
.mobile .divider i{width:55px}
.mobile .divider .brand{font-size:3.6px}
.m-gpp{left:0;top:390px;width:100%;height:109px;background:linear-gradient(90deg,#cfd8de 0%,#eef3f6 45%,#d9eef4 75%,#a5e0ee 100%)}
.m-foot{left:0;top:695px;width:100%;height:194px;background:var(--navy);color:#cfd3da;text-align:center;font-size:5.2px}
</style>
</head>
<body>

<!-- ================= DESKTOP ================= -->
<main class="screen desktop">
  <div class="abs topbar">
    <span style="left:37px">
      <svg width="5" height="5" viewBox="0 0 10 10"><path d="M2 1l2 2-1 1.5a6 6 0 002.5 2.5L7 6l2 2-1.5 1.5C4 9 1 6 .5 2.5z" fill="none" stroke="#ec1f27" stroke-width="1"/></svg>
      Contact us on <b>0330 555 0142</b>
    </span>
    <span style="left:126px">
      <svg width="6" height="5" viewBox="0 0 12 9"><rect x=".5" y=".5" width="11" height="8" fill="none" stroke="#ec1f27"/><path d="M.5 .5l5.5 4.5 5.5-4.5" fill="none" stroke="#ec1f27"/></svg>
      Email: info@quorvanta.co.uk
    </span>
    <div class="dots"><i class="dot"></i><i class="dot"></i><i class="dot"></i><i class="dot"></i></div>
  </div>

  <header class="abs nav">
    <div class="abs" style="left:37px;top:7px">
      <div class="brand" style="font-size:8.5px">QUORVANTA</div>
      <div class="brand-sub" style="margin-left:6px">PHARMACOVIGILANCE</div>
    </div>
    <ul>
      <li class="active">Home</li><li>About Us</li><li>QPPV</li><li>Our Services</li><li>Contact Us</li><li>Client</li>
    </ul>
  </header>

  <section class="photo hero" role="img" aria-label="Photo of two doctors in white coats talking and smiling">
    <div class="hero-text">
      <div class="kicker">Pharmacovigilance</div>
      <div class="title">Outsourcing Partner</div>
      <p class="lead">At Quorvanta we ensure that your business has the best<br>Pharmacovigilance support in the industry</p>
      <span class="btn">&#8595; Company Brochure</span>
    </div>
  </section>

  <div class="divider" style="top:261px"><i></i><span class="brand">QUORVANTA</span><i></i></div>
  <h2 class="heading" style="top:280px">Welcome to the <em>Quorvanta Pharmacovigilance</em></h2>
  <p class="para" style="left:90px;width:261px;top:302px">Welcome to the Quorvanta Pharmacovigilance website. We are an outsourcing partner to large and small companies within the pharmaceutical industry. Our range of services is tailored to suit each of our client's needs and cover both human and veterinary medicinal products.</p>

  <article class="card is-active" style="left:75px">
    <div class="icon"><svg width="13" height="13" viewBox="0 0 20 20"><circle cx="10" cy="10" r="8" fill="none" stroke="#9aa" stroke-width="1"/><rect x="6" y="6" width="8" height="5" rx="2.5" transform="rotate(-35 10 8.5)" fill="none" stroke="#9aa"/><circle cx="12" cy="13" r="2.5" fill="none" stroke="#9aa"/></svg></div>
    <h3>Medical Information</h3>
    <p>Professional enquiry handling to support the safe and effective use of your products.</p>
  </article>
  <article class="card" style="left:149px">
    <div class="icon"><svg width="13" height="13" viewBox="0 0 20 20"><path d="M10 17S2 12 2 7a4 4 0 018-1 4 4 0 018 1c0 5-8 10-8 10z" fill="none" stroke="#fff" stroke-width="1.3"/><path d="M10 7v4M10 12.5v.5" stroke="#fff" stroke-width="1.3"/></svg></div>
    <h3>Pharmacovigilance</h3>
    <p>Ease the regulatory burden and keep compliant with current pharmacovigilance legislation.</p>
  </article>
  <article class="card" style="left:224px">
    <div class="icon"><svg width="13" height="13" viewBox="0 0 20 20"><rect x="4" y="3" width="11" height="14" fill="none" stroke="#fff" stroke-width="1.2"/><path d="M7 7h5M7 10h5M7 13h3" stroke="#fff" stroke-width="1.2"/></svg></div>
    <h3>Literature Monitoring</h3>
    <p>Product safety through surveillance of published articles and case reports.</p>
  </article>
  <article class="card" style="left:298px">
    <div class="icon"><svg width="13" height="13" viewBox="0 0 20 20"><circle cx="9" cy="6" r="3.2" fill="none" stroke="#fff" stroke-width="1.2"/><path d="M3 17c0-4 3-6 6-6s6 2 6 6z" fill="none" stroke="#fff" stroke-width="1.2"/><circle cx="15" cy="14" r="2.6" fill="#ec1f27" stroke="#fff"/></svg></div>
    <h3>Training</h3>
    <p>Confident staff to support the pharmacovigilance process.</p>
  </article>

  <section class="photo gpp" role="img" aria-label="Photo of laboratory scientists in safety glasses working with pipettes and a laptop">
    <div class="gpp-text">
      <div class="kicker">Good Pharmacovigilance</div>
      <div class="title">Practice</div>
      <p class="lead">At Quorvanta we ensure that your business has the best<br>Pharmacovigilance support in the industry</p>
      <span class="btn">&#8595; Company Brochure</span>
    </div>
  </section>

  <div class="divider" style="top:706px"><i></i><span class="brand">QUORVANTA</span><i></i></div>
  <h2 class="heading" style="top:724px">Qualified Person for <em>Pharmacovigilance</em></h2>
  <p class="para" style="left:110px;width:221px;top:746px">Pharmaceutical companies who intend to market their medicinal products in the European Union must first apply for a Marketing Authorisation (MA)</p>

  <div class="person" style="left:69px;top:777px"><div class="avatar"><div role="img" aria-label="Portrait photo of staff member Clara"></div></div><h4>Clara</h4><p>Confident staff to<br>support the</p></div>
  <div class="person" style="left:180px;top:777px"><div class="avatar"><div role="img" aria-label="Portrait photo of staff member Owen"></div></div><h4>Owen</h4><p>Confident staff to<br>support the</p></div>
  <div class="person" style="left:292px;top:777px"><div class="avatar"><div role="img" aria-label="Portrait photo of staff member Nadia"></div></div><h4>Nadia</h4><p>Confident staff to<br>support the</p></div>

  <footer class="abs footer">
    <div class="abs" style="left:37px;top:28px"><div class="brand" style="font-size:8.5px">QUORVANTA</div></div>
    <p class="abs" style="left:38px;top:65px">Link to our VERA platform.</p>
    <div class="abs social" style="left:38px;top:84px"><i></i><i></i><i></i><i></i></div>

    <h5 class="abs" style="left:149px;top:26px">Our Location</h5>
    <svg class="abs" style="left:149px;top:46px" width="6" height="7" viewBox="0 0 10 12"><path d="M5 11S1 7 1 4.5a4 4 0 018 0C9 7 5 11 5 11z" fill="none" stroke="#fff"/><circle cx="5" cy="4.5" r="1.4" fill="none" stroke="#fff"/></svg>
    <p class="abs" style="left:162px;top:46px;line-height:1.8">Our offices are situated in<br>Harbour Court,<br>Ashwell, Northbridge.</p>
    <p class="abs" style="left:162px;top:77px">For directions <a>click here.</a></p>

    <h5 class="abs" style="left:261px;top:26px">Contact Details</h5>
    <p class="abs" style="left:261px;top:46px;line-height:2">&#9990;&nbsp; 0330 555 0142<br>&#9993;&nbsp; info@quorvanta.co.uk</p>

    <h5 class="abs" style="right:37px;top:26px">Quick Links</h5>
    <ul class="abs" style="right:37px;top:45px"><li>Home</li><li>About Us</li><li>QPPV</li><li>Our Services</li><li>Contact Us</li><li>Client</li></ul>
  </footer>
  <div class="abs copy" style="top:1033px;height:24px;line-height:24px;font-size:4.4px">Copyright © 2020 Quorvanta Ltd <span style="color:#cfd3da">(Registered in England &amp;Wales : 08214467)</span></div>
</main>

<!-- ================= MOBILE ================= -->
<main class="screen mobile">
  <header class="abs m-head">
    <div class="abs" style="left:13px;top:22px">
      <div class="brand" style="font-size:7.5px">QUORVANTA</div>
      <div class="brand-sub" style="margin-left:5px;font-size:2.4px">PHARMACOVIGILANCE</div>
    </div>
    <svg class="abs" style="left:130px;top:30px" width="8" height="8" viewBox="0 0 10 10"><path d="M2 1l2 2-1 1.5a6 6 0 002.5 2.5L7 6l2 2-1.5 1.5C4 9 1 6 .5 2.5z" fill="none" stroke="#111" stroke-width=".8"/></svg>
    <svg class="abs" style="left:145px;top:31px" width="8" height="6" viewBox="0 0 12 9"><rect x=".5" y=".5" width="11" height="8" fill="none" stroke="#111"/><path d="M.5 .5l5.5 4.5 5.5-4.5" fill="none" stroke="#111"/></svg>
    <svg class="abs" style="left:161px;top:31px" width="7" height="6" viewBox="0 0 7 6"><path d="M0 .5h7M0 3h7M0 5.5h7" stroke="#111" stroke-width=".9"/></svg>
  </header>

  <section class="photo m-hero" role="img" aria-label="Photo of two doctors in white coats talking and smiling">
    <div class="hero-text" style="left:11px;top:15px">
      <div class="kicker">Pharmacovigilance</div>
      <div class="title">Outsourcing<br>Partner</div>
      <p class="lead">At Quorvanta we ensure that your business has the best<br>Pharmacovigilance support in the industry</p>
      <span class="btn">&#8595; Company Brochure</span>
    </div>
  </section>

  <div class="divider" style="top:179px"><i></i><span class="brand">QUORVANTA</span><i></i></div>
  <h2 class="heading" style="top:193px">Welcome to the<br><em>Quorvanta Pharmacovigilance</em></h2>
  <p class="para" style="left:20px;width:141px;top:220px">Welcome to the Quorvanta Pharmacovigilance website. We are an outsourcing partner to large and small companies within the pharmaceutical industry. Our range of services is tailored to suit each of our client's needs and cover both human and veterinary medicinal products.</p>

  <article class="card is-active" style="left:20px">
    <div class="icon"><svg width="12" height="12" viewBox="0 0 20 20"><circle cx="10" cy="10" r="8" fill="none" stroke="#9aa"/><rect x="6" y="6" width="8" height="5" rx="2.5" transform="rotate(-35 10 8.5)" fill="none" stroke="#9aa"/></svg></div>
    <h3>Medical Information</h3>
    <p>Professional enquiry handling to support the safe and effective use of your products.</p>
  </article>
  <article class="card" style="left:95px">
    <div class="icon"><svg width="12" height="12" viewBox="0 0 20 20"><path d="M10 17S2 12 2 7a4 4 0 018-1 4 4 0 018 1c0 5-8 10-8 10z" fill="none" stroke="#fff" stroke-width="1.3"/><path d="M10 7v4M10 12.5v.5" stroke="#fff" stroke-width="1.3"/></svg></div>
    <h3>Pharmacovigilance</h3>
    <p>Ease the regulatory burden and keep compliant with current pharmacovigilance legislation.</p>
  </article>

  <section class="photo m-gpp" role="img" aria-label="Photo of laboratory scientists in safety glasses working with pipettes and a laptop">
    <div class="gpp-text" style="right:15px;top:13px">
      <div class="kicker">Good<br>Pharmacovigilance</div>
      <div class="title">Practice</div>
      <p class="lead">At Quorvanta we ensure that<br>your business has</p>
      <span class="btn">&#8595; Company Brochure</span>
    </div>
  </section>

  <div class="divider" style="top:514px"><i></i><span class="brand">QUORVANTA</span><i></i></div>
  <h2 class="heading" style="top:528px">Qualified Person<br>for <em>Pharmacovigilance</em></h2>
  <p class="para" style="left:10px;width:161px;top:555px">Pharmaceutical companies who intend to market their medicinal products in the European Union must first apply for a Marketing Authorisation (MA)</p>

  <div class="person" style="left:50px;top:580px"><div class="avatar" style="width:66px;height:66px"><div role="img" aria-label="Portrait photo of staff member Owen"></div></div><h4 style="margin-top:13px">Owen</h4><p>Confident staff to<br>support the</p></div>

  <footer class="abs m-foot">
    <div class="brand" style="font-size:11px;margin-top:25px">QUORVANTA</div>
    <p style="margin-top:10px">Link to our VERA platform.</p>
    <div class="social" style="justify-content:center;margin-top:14px;gap:11px"><i></i><i></i><i></i><i></i></div>
    <p style="margin-top:14px;line-height:1.75">Our offices are situated in Harbour Court,<br>Ashwell, Northbridge.</p>
    <p style="margin-top:9px">For directions <a style="color:#fff;text-decoration:underline">click here.</a></p>
    <p style="margin-top:27px">&#9990; 0330 555 0142 &nbsp;&nbsp;&nbsp; &#9993; info@quorvanta.co.uk</p>
  </footer>
  <div class="abs copy" style="top:889px;height:39px;padding-top:9px;font-size:5.2px;line-height:1.75">Copyright © 2020 Quorvanta Ltd<br><span style="color:#cfd3da">(Registered in England &amp;Wales : 08214467)</span></div>
</main>

</body>
</html>
```